Commercial Construction Interior Fitout company needs Logo and Business Cards

We need a logo and business card design. We specialise in Commercial Ceilings, Partitions, Plastering and Carpentry.

Company name: 7QX Commercial Interiors. Would like a professional looking card more than a fancy look. Gloss front preferably black pattern with Fluro Green and white text.

Will need:

Name
Position
Phone
Fax
Email
Postal Address
Web address
Updates

Thank you so much everyone for your efforts and fantastic designs..   If I didn't respond to everyone personally,  my apologises. 

Again, thanks all

R.M                               

Target Market(s)

Existing & New clients in the Construction Industry

Industry/Entity Type

Business

Requirements
Nice to have
• 7QX to be overlapped or made into some sort of Logo

```html
<!DOCTYPE html>
<html lang="en">
<head>
<meta charset="utf-8">
<title>7QX Commercial Interiors – Business Card</title>
<link rel="stylesheet" href="https://fonts.googleapis.com/css2?family=Questrial&display=swap">
<style>
  :root {
    --backdrop: #e6e4e0;
    --card-black: #000000;
    --texture-dark: #0a0a0a;
    --fluro-green: #5ed200;
    --white: #ffffff;
    --soft-white: #d9d9d9;
  }
  * { margin: 0; padding: 0; box-sizing: border-box; }
  html, body {
    width: 1200px;
    height: 900px;
    overflow: hidden;
    background: var(--backdrop);
    font-family: "Questrial", "Century Gothic", sans-serif;
  }
  .canvas {
    position: relative;
    width: 1200px;
    height: 900px;
  }
  .card {
    position: absolute;
    top: 152px;
    width: 381px;
    height: 624px;
    background: var(--card-black);
    overflow: hidden;
    box-shadow: 0 4px 14px rgba(0,0,0,0.25);
  }
  .card--front { left: 130px; }
  .card--back { left: 666px; }
  .card__texture {
    position: absolute;
    inset: 0;
    background: linear-gradient(160deg, var(--texture-dark), var(--card-black) 70%);
  }

  /* Front */
  .front-lockup {
    position: absolute;
    left: 0;
    right: 0;
    top: 405px;
    height: 120px;
    display: flex;
  }
  .front-lockup__square {
    width: 88px;
    height: 100%;
    background: var(--white);
  }
  .front-lockup__band {
    flex: 1;
    height: 100%;
    background: var(--fluro-green);
    display: flex;
    align-items: center;
    justify-content: flex-end;
    padding-right: 8px;
  }
  .front-lockup__name {
    color: var(--card-black);
    font-size: 22px;
    line-height: 1.2;
    letter-spacing: 1.5px;
    text-align: right;
  }

  /* Back */
  .back-lockup {
    position: absolute;
    left: 0;
    top: 0;
    display: flex;
    align-items: center;
  }
  .back-lockup__square {
    width: 34px;
    height: 122px;
    background: var(--fluro-green);
  }
  .back-lockup__name {
    color: var(--white);
    font-size: 76px;
    line-height: 1;
    padding-left: 14px;
    letter-spacing: 2px;
  }
  .contact {
    position: absolute;
    right: 35px;
    top: 294px;
    text-align: right;
    color: var(--soft-white);
    font-size: 16px;
    line-height: 21px;
    letter-spacing: 0.6px;
  }
  .contact__name {
    color: var(--fluro-green);
    font-size: 24px;
    line-height: 26px;
    letter-spacing: 1.5px;
  }
  .contact__role { margin-bottom: 56px; }
  .contact__block + .contact__block { margin-top: 19px; }
</style>
</head>
<body>
<main class="canvas">

  <section class="card card--front" aria-label="Business card front">
    <div class="card__texture" role="img" aria-label="Faint repeated brand pattern on black"></div>
    <div class="front-lockup">
      <span class="front-lockup__square"></span>
      <div class="front-lockup__band">
        <p class="front-lockup__name">7QX<br>Commercial<br>Interiors</p>
      </div>
    </div>
  </section>

  <section class="card card--back" aria-label="Business card back">
    <div class="card__texture" role="img" aria-label="Faint repeated brand pattern on black"></div>
    <div class="back-lockup">
      <span class="back-lockup__square"></span>
      <p class="back-lockup__name">7QX</p>
    </div>
    <div class="contact">
      <p class="contact__name">LIAM CARTER</p>
      <p class="contact__role">Business Manager</p>
      <div class="contact__block">
        <p>2480 Ridgeway</p>
        <p>Harbour Vale 16809</p>
        <p>Australia</p>
      </div>
      <div class="contact__block">
        <p>Ph +0298765432</p>
        <p>Fax +0298765433</p>
      </div>
      <div class="contact__block">
        <p>www.7qxinteriors.com</p>
        <p>info@7qxinteriors.com</p>
      </div>
    </div>
  </section>

</main>
</body>
</html>
```